Truck and Van wrap design

We need designs for our trucks and vans. Our Logo and contact details including phone number (+97148517300), email (hello@zelvoraproduce.com), and website have to be incorporated into the design. Our company colors are white, green, red, and yellow in the same shades used in the logo. This design needs to be in .ai (Adobe Illustrator) format. We have 5 different size vehicles that need designs. We would prefer a scalable design that we can resize for future use.Truck 1 DimentionsHeight: 2.1 MetersWidth: 2.1 MetersLength: 5 MetersTruck 2 DimensionsHeight: 2.1 MetersWidth: 2.1 MetersLength: 4.3 MetersTruck 3 DimensionsHeight: 2.75 MetersWidth: 2.6 MetersLength: 7 MetersTrailer DimensionsHeight: 2.5 MetersWidth: 2.6 MetersLength: 13.58 MetersVan DimensionsHeight: 1.7 Meters Width: 1.7 MetersLength: 3.5 MetersYou can find pictures of the vehicles and our logo attached for reference. The trucks and trailer only need the two sides and back end designed while the van is a full wrap.
Please try to keep the designs clean and avoid the use of too many photos.

```html
<!DOCTYPE html>
<html lang="en">
<head>
<meta charset="utf-8">
<title>Zelvora Produce – Van Wrap</title>
<link rel="stylesheet" href="https://fonts.googleapis.com/css2?family=Montserrat:wght@400;800&family=Oswald:wght@400&display=swap">
<style>
  :root {
    --canvas: #e4e0db;
    --wrap-red: #b5302a;
    --wrap-red-deep: #962523;
    --wrap-orange: #f5a72b;
    --wrap-green: #8bbd3a;
    --wrap-white: #ffffff;
    --window: #efefef;
    --brand-ink: #3a3a3a;
  }
  html, body {
    margin: 0;
    padding: 0;
    width: 1200px;
    height: 1200px;
    overflow: hidden;
    background: var(--canvas);
  }
  .wrap-sheet { display: block; width: 1200px; height: 1200px; }
  .fill-red { fill: url(#redShade); }
  .fill-red-flat { fill: var(--wrap-red); }
  .fill-orange { fill: var(--wrap-orange); }
  .fill-green { fill: var(--wrap-green); }
  .fill-white { fill: var(--wrap-white); }
  .fill-window { fill: var(--window); }
  .brand-dot { fill: var(--wrap-red); }
  .brand-name {
    font-family: "Montserrat", sans-serif;
    font-weight: 400;
    fill: var(--brand-ink);
    letter-spacing: 3px;
  }
  .contact-phone {
    font-family: "Oswald", sans-serif;
    font-weight: 400;
    fill: var(--wrap-white);
  }
  .contact-company, .contact-line {
    font-family: "Montserrat", sans-serif;
    font-weight: 800;
    fill: var(--wrap-white);
  }
</style>
</head>
<body>
<svg class="wrap-sheet" viewBox="0 0 1500 1500" xmlns="http://www.w3.org/2000/svg">
  <defs>
    <linearGradient id="redShade" x1="0" y1="0" x2="1" y2="0.4">
      <stop offset="0" stop-color="#962523"/>
      <stop offset="0.35" stop-color="#b5302a"/>
      <stop offset="1" stop-color="#b5302a"/>
    </linearGradient>
    <path id="vanSideOutline" d="M215,413 L790,413 Q850,415 930,515 L930,682 Q930,690 922,690 L870,690 A73 73 0 0 0 726,725 L415,725 A72 72 0 0 0 271,715 L203,712 L200,678 L172,675 L170,640 L172,470 Q180,413 215,413 Z"/>
    <clipPath id="vanSideClip"><use href="#vanSideOutline"/></clipPath>
    <path id="vanBackOutline" d="M1085,413 L1290,413 Q1303,415 1305,430 L1330,597 L1312,606 L1310,705 Q1308,725 1290,725 L1082,725 Q1062,725 1060,705 L1060,606 L1042,600 L1070,430 Q1072,415 1085,413 Z"/>
    <clipPath id="vanBackClip"><use href="#vanBackOutline"/></clipPath>
  </defs>

  <!-- Van side, driver facing right -->
  <g class="van-side van-side--right">
    <g clip-path="url(#vanSideClip)">
      <rect class="fill-red" x="160" y="400" width="780" height="340"/>
      <path class="fill-orange" d="M443,400 C470,560 650,665 940,660 L940,400 Z"/>
      <path class="fill-white" d="M492,400 C520,540 680,650 940,645 L940,400 Z"/>
      <path class="fill-green" d="M548,540 C620,620 780,645 940,598 L940,628 C780,652 620,635 548,540 Z"/>
      <path class="fill-window" d="M720,433 L800,433 Q840,437 905,515 Q910,530 895,530 L740,517 Q733,516 733,505 Z"/>
    </g>
    <g class="brand-lockup">
      <circle class="brand-dot" cx="632" cy="478" r="22"/>
      <text class="brand-name" x="632" y="540" font-size="25" text-anchor="middle">ZELVORA</text>
    </g>
    <g class="contact-block">
      <text class="contact-phone" x="200" y="483" font-size="36">(+97148517300)</text>
      <text class="contact-company" x="200" y="535" font-size="20">Zelvora Produce</text>
      <text class="contact-company" x="200" y="559" font-size="20">General Trading LLC</text>
      <text class="contact-line" x="200" y="588" font-size="13.5">Email: hello@zelvoraproduce.com</text>
      <text class="contact-line" x="200" y="612" font-size="13.5">www.zelvoraproduce.com</text>
    </g>
  </g>

  <!-- Van side, driver facing left -->
  <g class="van-side van-side--left">
    <g transform="translate(1100,360) scale(-1,1)">
      <g clip-path="url(#vanSideClip)">
        <rect class="fill-red" x="160" y="400" width="780" height="340"/>
        <path class="fill-orange" d="M443,400 C470,560 650,665 940,660 L940,400 Z"/>
        <path class="fill-white" d="M492,400 C520,540 680,650 940,645 L940,400 Z"/>
        <path class="fill-green" d="M548,540 C620,620 780,645 940,598 L940,628 C780,652 620,635 548,540 Z"/>
        <path class="fill-window" d="M720,433 L800,433 Q840,437 905,515 Q910,530 895,530 L740,517 Q733,516 733,505 Z"/>
      </g>
    </g>
    <g class="brand-lockup">
      <circle class="brand-dot" cx="468" cy="838" r="22"/>
      <text class="brand-name" x="468" y="900" font-size="25" text-anchor="middle">ZELVORA</text>
    </g>
    <g class="contact-block" text-anchor="end">
      <text class="contact-phone" x="900" y="843" font-size="36">(+97148517300)</text>
      <text class="contact-company" x="900" y="895" font-size="20">Zelvora Produce</text>
      <text class="contact-company" x="900" y="919" font-size="20">General Trading LLC</text>
      <text class="contact-line" x="900" y="948" font-size="13.5">Email: hello@zelvoraproduce.com</text>
      <text class="contact-line" x="900" y="972" font-size="13.5">www.zelvoraproduce.com</text>
    </g>
  </g>

  <!-- Van rear doors -->
  <g class="van-rear">
    <g clip-path="url(#vanBackClip)">
      <rect class="fill-white" x="1035" y="405" width="305" height="330"/>
      <path class="fill-orange" d="M1035,538 C1100,625 1260,635 1340,540 L1340,740 L1035,740 Z"/>
      <path class="fill-red-flat" d="M1035,575 C1100,635 1265,640 1340,553 L1340,740 L1035,740 Z"/>
      <path class="fill-green" d="M1150,598 C1250,600 1300,570 1324,520 L1328,545 C1300,592 1240,603 1150,598 Z"/>
    </g>
    <g class="brand-lockup">
      <circle class="brand-dot" cx="1186" cy="486" r="21"/>
      <text class="brand-name" x="1186" y="545" font-size="22" text-anchor="middle">ZELVORA</text>
    </g>
    <g class="contact-block" text-anchor="middle">
      <text class="contact-phone" x="1186" y="654" font-size="24">(+97148517300)</text>
      <text class="contact-company" x="1186" y="674" font-size="10">Zelvora Produce</text>
      <text class="contact-company" x="1186" y="686" font-size="10">General Trading LLC</text>
      <text class="contact-line" x="1186" y="699" font-size="6.5">Email: hello@zelvoraproduce.com</text>
      <text class="contact-line" x="1186" y="711" font-size="6.5">www.zelvoraproduce.com</text>
    </g>
  </g>

  <!-- Van roof / hood panel -->
  <g class="van-hood">
    <rect class="fill-white" x="1042" y="832" width="288" height="114"/>
    <g class="brand-lockup">
      <circle class="brand-dot" cx="1186" cy="872" r="19"/>
      <text class="brand-name" x="1186" y="921" font-size="18" text-anchor="middle">ZELVORA</text>
    </g>
  </g>
</svg>
</body>
</html>
```